TriVex Business Card Design - double sided -plumbing local plumbing company

We have a Plumbing company where the design was create through Sketch Hive. We would now like a business card designed as well. We want it to be in the colour version of the logo.

Details below for the card.

Phone Number: 0438 615 247
Email: info@trivexplumbing.example.au
Website: https://trivexplumbing.example.au
We really want a sophisticated design that stand out from the other- informative and timeless.

Target Market(s)

local Canberra market

Industry/Entity Type

Plumbing, gas fitting, hot water

Contact Information for Business Card

Phone number, email, logo and "Supplying all your heating, cooling and hot water needs"

Requirements
Must have
• bust be colourful, must also be though about it being printed on a magnet. must Vex with the logo - I dont want the logo and information chucked onto a white canvas I would prefer it to be smooth and look purposeful

```html
<!DOCTYPE html>
<html lang="en">
<head>
<meta charset="utf-8">
<title>TriVex Business Card</title>
<link href="https://fonts.googleapis.com/css2?family=Poppins:wght@400;600;700&display=swap" rel="stylesheet">
<style>
  :root{
    --bg:#1c1c1c;
    --orange:#fbb040;
    --blue:#00aeef;
    --white:#ffffff;
    --ink:#1a1a1a;
  }
  html,body{margin:0;padding:0;overflow:hidden}
  body{width:1200px;height:1015px;background:var(--bg);font-family:"Poppins",sans-serif;position:relative}
  .card{position:absolute;left:300px;width:600px;height:343px;overflow:hidden;box-shadow:0 12px 30px rgba(0,0,0,.6)}
  .card--front{top:120px}
  .card--back{top:540px;background:var(--white)}
  .card__waves{position:absolute;inset:0;width:100%;height:100%}
  .tagline{position:absolute;left:46px;top:70px;margin:0;color:var(--white);font-weight:600;font-size:19px;line-height:1.3;letter-spacing:.5px;text-transform:uppercase}
  .wordmark{position:absolute;margin:0;font-weight:700;letter-spacing:1px;color:var(--blue)}
  .card--front .wordmark{right:40px;bottom:42px;font-size:64px;color:#0b98d2}
  .card--back .wordmark{left:44px;top:92px;font-size:62px}
  .person{position:absolute;right:46px;top:28px;text-align:right}
  .person__name{margin:0;font-weight:700;font-size:20px;letter-spacing:.5px;text-transform:uppercase;color:var(--blue);line-height:1.3}
  .person__name span{color:var(--orange)}
  .person__role{margin:0;font-size:15px;color:var(--ink);line-height:1.4}
  .person__marker{position:absolute;right:0;top:30px;width:18px;height:26px;background:var(--orange)}
  .contact{position:absolute;right:32px;bottom:32px;list-style:none;margin:0;padding:0;text-align:right}
  .contact li{color:var(--white);font-size:16px;line-height:1.75;display:flex;justify-content:flex-end;align-items:center;gap:10px}
  .contact svg{width:16px;height:16px;flex:none}
</style>
</head>
<body>

<section class="card card--front">
  <svg class="card__waves" viewBox="0 0 600 343" preserveAspectRatio="none" aria-hidden="true">
    <rect width="600" height="343" fill="var(--blue)"/>
    <path d="M0,0 H600 V80 C500,55 430,70 350,150 C270,230 170,290 0,300 Z" fill="var(--orange)"/>
    <path d="M40,292 C180,285 270,225 350,150 C430,72 500,52 560,58" fill="none" stroke="var(--blue)" stroke-width="4"/>
    <path d="M60,300 C200,292 290,232 370,158 C450,84 520,66 590,75" fill="none" stroke="var(--orange)" stroke-width="4"/>
  </svg>
  <p class="tagline">Supplying all your heating<br>cooling and hot water needs</p>
  <p class="wordmark">TriVex</p>
</section>

<section class="card card--back">
  <svg class="card__waves" viewBox="0 0 600 343" preserveAspectRatio="none" aria-hidden="true">
    <path d="M0,272 C140,284 230,244 300,186 C380,128 470,125 600,125 V343 H0 Z" fill="var(--blue)"/>
    <path d="M0,250 C140,262 222,222 292,164 C372,106 462,105 560,105" fill="none" stroke="var(--orange)" stroke-width="7"/>
    <path d="M0,262 C140,274 226,234 296,176 C376,118 466,115 590,115" fill="none" stroke="var(--orange)" stroke-width="5"/>
  </svg>
  <p class="wordmark">TriVex</p>
  <div class="person">
    <p class="person__name">Marcus <span>Reilly</span></p>
    <p class="person__role">Managing Director</p>
  </div>
  <div class="person__marker"></div>
  <ul class="contact">
    <li>0438 615 247
      <svg viewBox="0 0 16 16"><path d="M3 1.5l3 .5 1 3-1.8 1.3a9 9 0 0 0 4.5 4.5L11 9l3 1 .5 3-2 1.5C7 14 2 9 1.5 3.5z" fill="var(--orange)"/></svg></li>
    <li>info@trivexplumbing.example.au
      <svg viewBox="0 0 16 16"><rect x="1" y="3" width="14" height="10" fill="var(--orange)"/><path d="M1 3l7 6 7-6" fill="none" stroke="var(--white)" stroke-width="1.2"/></svg></li>
    <li>www.trivexplumbing.example.au
      <svg viewBox="0 0 16 16"><g fill="none" stroke="var(--orange)" stroke-width="1.4"><circle cx="8" cy="8" r="6.5"/><ellipse cx="8" cy="8" rx="3" ry="6.5"/><path d="M1.5 8h13M2.5 5h11M2.5 11h11"/></g></svg></li>
  </ul>
</section>

</body>
</html>
```